New flavour! New packaging for Velocity Energy Drink!

We need a new packaging designed to show off our new grape flavored energy drink! It will require box design with matching sachets!

Established in 2018 we are a fully Australian owned and operated business that started out with 2 gamers that got sick and tired of sugary energy drinks OR expensive powder from the USA.

We are an energy drink in the esports and gaming space. Our new product is an energy drink in powder in boxes of 30 sachets (please see attached for product example)

Please see example 1 and 2 for our competitors product. We would ideally like to go a bit more minimalist than them but still have a great color pop on black backing.

Target Market(s)

Gamer's and esports athletes between the ages or 18-30

Font styles to use
Sans Serif
Other font styles liked:
• Helvetica

Colors
886aae
ffffff

Requirements
Must have
• Black base/background.
• Vibrant purple N in the Velocity Logo.
• Same or slightly different shades of purple for some text and highlights.
• Black, white and some shades of a vibrant purple (for the grape flavor)
• ingredients list (may need to be reformatted to suit)
• Please see attached for legislative requirements on the box and sachets.
Nice to have
• minimalist design but enough to be eye catching and somewhat playful
• Twitter: @VLCT_FUEL
• Instagram: @VLCT_FUEL
• Facebook: @VLCTFUEL
Should not have
• OTHER COLORS.
• Overly complex designs.

```html
<!DOCTYPE html>
<html lang="en">
<head>
<meta charset="utf-8">
<title>Velocity Energy Drink – Grape Box Dieline</title>
<link rel="stylesheet" href="https://fonts.googleapis.com/css2?family=Raleway:wght@300;400;700&family=Open+Sans:wght@400;700&family=Montserrat:wght@900&display=swap">
<style>
  :root {
    --page: #ffffff;
    --box: #000000;
    --side: #1a1a1a;
    --side-mark: #262626;
    --white: #ffffff;
    --soft-white: #cfcfcf;
    --grape: #7a5cff;
    --grape-light: #b29bff;
    --table-line: #000000;
  }
  * { margin: 0; padding: 0; box-sizing: border-box; }
  html, body { width: 999px; height: 1200px; overflow: hidden; background: var(--page); }
  .canvas { position: relative; width: 999px; height: 1200px; }

  .dieline {
    position: absolute; left: 20px; top: 315px;
    width: 960px; height: 571px;
    display: flex;
  }
  .panel { position: relative; height: 100%; overflow: hidden; }
  .panel--side { width: 211px; background: var(--side); }
  .panel--front, .panel--back { width: 269px; background: var(--box); }

  /* Side panels */
  .side-name {
    position: absolute; left: 50%; top: 50%;
    transform: translate(-50%, -50%) rotate(-90deg);
    font-family: "Montserrat", sans-serif; font-weight: 900;
    font-size: 72px; letter-spacing: 2px;
    color: var(--side-mark); white-space: nowrap;
  }

  /* Front panel */
  .grapes { position: absolute; }
  .grapes--top {
    left: 168px; top: 0; width: 101px; height: 137px;
    background: linear-gradient(200deg, var(--grape-light), var(--grape));
    border-bottom-left-radius: 60px;
  }
  .grapes--bottom {
    left: 0; top: 372px; width: 164px; height: 122px;
    background: linear-gradient(160deg, var(--grape), var(--grape-light));
    border-top-right-radius: 70px;
  }
  .brand {
    position: absolute; left: 0; top: 156px; width: 269px; height: 37px;
    display: flex; align-items: center; gap: 8px; padding-left: 12px;
  }
  .brand__dot { width: 10px; height: 10px; background: var(--grape); }
  .brand__name {
    font-family: "Raleway", sans-serif; font-weight: 700;
    font-size: 26px; letter-spacing: 3px; color: var(--grape);
  }
  .flavour {
    position: absolute; left: 52px; top: 226px;
    font-family: "Raleway", sans-serif; font-weight: 300;
    font-size: 25px; line-height: 30px; color: var(--white);
  }
  .flavour .grape-word { color: var(--grape); }
  .flavour .energy-word { color: var(--grape-light); margin-right: 14px; }
  .tagline {
    position: absolute; left: 52px;
    font-family: "Raleway", sans-serif; font-weight: 300;
    font-size: 15px; color: var(--white);
  }
  .tagline--ingredients { top: 304px; color: var(--soft-white); }
  .tagline--motto { top: 338px; }
  .pack-facts {
    position: absolute; right: 11px; top: 500px; text-align: right;
    font-family: "Raleway", sans-serif; font-weight: 300; color: var(--white);
  }
  .pack-facts__serves { font-size: 15px; margin-bottom: 5px; }
  .pack-facts__line { font-size: 12px; line-height: 14px; }

  /* Back panel */
  .nutrition {
    position: absolute; left: 16px; top: 13px; width: 236px;
    border-collapse: collapse; background: var(--white);
    font-family: "Open Sans", sans-serif; font-size: 5.6px; color: #000;
  }
  .nutrition td, .nutrition th {
    border: 0.6px solid var(--table-line);
    padding: 1.6px 3px; line-height: 6.4px; font-weight: 400;
  }
  .nutrition .title th { text-align: left; font-weight: 700; font-size: 6px; }
  .nutrition .col-head th { font-weight: 700; text-align: center; }
  .nutrition .num { text-align: right; }
  .nutrition .indent { padding-left: 22px; }
  .nutrition .subhead td { font-weight: 700; }
  .nutrition .spacer td { height: 9px; }

  .back-copy {
    position: absolute; left: 16px; top: 239px; width: 242px;
    font-family: "Raleway", sans-serif; font-weight: 300;
    font-size: 9.2px; line-height: 11.2px; color: var(--white);
  }
  .back-copy__product { font-size: 11px; margin-bottom: 10px; }
  .back-copy p { margin-bottom: 10px; }
  .back-copy .address { padding-left: 66px; }
</style>
</head>
<body>
<div class="canvas">
  <div class="dieline">

    <section class="panel panel--side">
      <span class="side-name">VELOCITY</span>
    </section>

    <section class="panel panel--front">
      <div class="grapes grapes--top" role="img" aria-label="Illustrated cluster of purple grapes with leaves"></div>
      <div class="brand">
        <span class="brand__dot"></span>
        <span class="brand__name">VELOCITY</span>
      </div>
      <div class="flavour">
        <div><span class="grape-word">Grape</span> flavour</div>
        <div><span class="energy-word">Energy</span> Drink</div>
      </div>
      <div class="tagline tagline--ingredients">With Ginseng &amp; Caffeine</div>
      <div class="tagline tagline--motto">For gamers, By gamers</div>
      <div class="grapes grapes--bottom" role="img" aria-label="Illustrated cluster of purple grapes with leaves"></div>
      <div class="pack-facts">
        <div class="pack-facts__serves">30 serves</div>
        <div class="pack-facts__line">Weight: 150 g (30 x 5 g)</div>
        <div class="pack-facts__line">Formulated Caffeinated Beverage</div>
      </div>
    </section>

    <section class="panel panel--side">
      <span class="side-name">VELOCITY</span>
    </section>

    <section class="panel panel--back">
      <table class="nutrition">
        <tr class="title"><th colspan="3">NUTRITION INFORMATION</th></tr>
        <tr><td>SERVINGS PER PACKAGE:</td><td colspan="2">30</td></tr>
        <tr><td>SERVING SIZE:</td><td colspan="2">5g powder &amp; 500 ml water</td></tr>
        <tr class="col-head"><th></th><th>AV QUANTITY<br>PER SERVING<br>(400 ml)</th><th>AV QUANTITY<br>PER 100 ml</th></tr>
        <tr><td>ENERGY</td><td class="num">5 kJ</td><td class="num">1 kJ</td></tr>
        <tr><td>PROTEIN</td><td class="num">0.0 g</td><td class="num">0.0 g</td></tr>
        <tr><td>FAT TOTAL</td><td class="num">0.0 g</td><td class="num">0.0 g</td></tr>
        <tr><td class="indent">Saturated Fat</td><td class="num">0.0 g</td><td class="num">0.0 g</td></tr>
        <tr><td>CARBOHYDRATE</td><td class="num">0.3 g</td><td class="num">0.1 g</td></tr>
        <tr><td class="indent">Sugars</td><td class="num">0.0 g</td><td class="num">0.0 g</td></tr>
        <tr><td>SODIUM</td><td class="num">250 mg</td><td class="num">62 mg</td></tr>
        <tr class="subhead"><td colspan="3">Composition Information</td></tr>
        <tr><td>Caffeine</td><td class="num">100 mg</td><td class="num">25 mg</td></tr>
        <tr><td>Thiamin (B1)</td><td class="num">10 mg</td><td class="num">2.5 mg</td></tr>
        <tr><td>Riboflavin (B2)</td><td class="num">5 mg</td><td class="num">1.2 mg</td></tr>
        <tr><td>Niacin (B3)</td><td class="num">20 mg</td><td class="num">5 mg</td></tr>
        <tr><td>B6 (Pyridoxine)</td><td class="num">5 mg</td><td class="num">1.2 mg</td></tr>
        <tr><td>Taurine</td><td class="num">500 mg</td><td class="num">125 mg</td></tr>
        <tr><td>Inositol</td><td class="num">50 mg</td><td class="num">12.5 mg</td></tr>
        <tr class="spacer"><td></td><td></td><td></td></tr>
      </table>

      <div class="back-copy">
        <div class="back-copy__product">Energy drink</div>
        <p>Ingredient listing: &nbsp; Acidity regulator (citric acid, sodium citrate), mineral salt (sodium bicarbonate), taurine, natural orange juice powder (8.5%) (maltodextrin, sugar, orange juice concentrate), caffeine (2.8%), inositol, vitamins (B3, B1, B6, B2), ginseng extract (0.5%), sweetener (steviol glycoside), mineral salt (magnesium stearate).</p>
        <p>Storage statement: Store in a cool dry place, away from sunlight below 25o C. Keep away from children</p>
        <p>Directions for Use: Place one tablet in 400 ml water, stir until dissolved, and consume immediately.</p>
        <p>Usage: Maximum of two tablets per day</p>
        <p>Best Before: See base of packaging</p>
        <p>Imported By: Play Fuel Labs Pty Ltd<br>
          <span class="address">42 Arcade Lane</span><br>
          <span class="address">Melbourne &nbsp;VIC &nbsp;3000</span><br>
          <span class="address">Australia</span><br>
          www.velocityfuel.shop</p>
        <p>Country of origin: Made in China</p>
      </div>
    </section>

  </div>
</div>
</body>
</html>
```